Packaging Design for Face Mask Box

We are looking for an attractive but subtle packaging design for Face Masks (for non medical use). 50pcs per box.

The brand name should be "Kelvano". We have not yet got a logo or a text selected (font) for the brand name so we are open to your ideas on how "Kelvano" could look. It could have some elements of fresh air or breathing etc so symbolize clean and healthier air or something along those lines.

The box dimensions should be 180mm (L) x 100mm (W) x 90mm (H).

The box should have a perforation on top - exactly similar to Tissue Box packs. So, in order to access the face masks, the user should tear off the perforation and extract one mask at a time.

As this is not a medical grade face mask, the product should indicate "For Non- Medical Use". Also the heading of the masks should be DISPOSABLE PROTECTIVE FACE MASKS with sub heading 3 PLY FACE MASKS WITH EAR LOOP.

We will also prefer to have the Instructions to use and Precautions which are commonly available on face mask packages. This could be printed either on the sides or on the bottom of the package. There should also be a blank space on one of the sides to print Batch No. Mfg Date and Exp Date.

The box design could have some design resemblance to our company logo which is hereby attached in high resolution. However this is not compulsory.

The following phrases could be mentioned on the box to highlight some of the product features:

Dual Charge Electrostatic fibres for extra filtration
Improved Nose Bridge Strips for better protection
Tri-layer barrier with 3 x 25 g/m2 material
In-house production of filter material for Quality Consistency

I have added 3 samples face mask box designs from other manufacturers for your reference to get an idea of the box shape etc.

If you have any more questions, please feel free to ask.

Good luck!

```html
<!DOCTYPE html>
<html lang="en">
<head>
<meta charset="utf-8">
<title>Kelvano Face Mask Box – Dieline</title>
<link href="https://fonts.googleapis.com/css2?family=Montserrat:wght@300;400;700&family=Open+Sans:ital,wght@1,600&family=Roboto+Condensed:wght@700&family=Roboto:wght@400&display=swap" rel="stylesheet">
<style>
  :root {
    --navy: #12325a;
    --blue: #3189c4;
    --blue-text: #3a8dc8;
    --shade: #d4dadd;
    --tick: #7bbf3a;
    --line: #222;
    --paper: #ffffff;
    --pattern-light: #4ea3d8;
    --pattern-dark: #0d3a68;
  }
  * { box-sizing: border-box; margin: 0; padding: 0; }
  html, body { width: 1200px; height: 1200px; overflow: hidden; background: var(--paper); }
  .canvas { position: relative; width: 1200px; height: 1200px; font-family: "Montserrat", sans-serif; }
  .dieline { position: absolute; inset: 0; width: 1200px; height: 1200px; }
  .dieline path, .dieline rect { fill: none; stroke: var(--line); stroke-width: 1; }
  .dieline .perforation { stroke-dasharray: 2 2; stroke: #333; }

  .lid-pattern {
    position: absolute; left: 61px; top: 337px; width: 133px; height: 182px;
    background: linear-gradient(160deg, #1f6fae 0%, #3a96d0 45%, rgba(180,215,238,0.6) 80%, rgba(220,236,247,0) 100%);
    clip-path: polygon(0 0, 100% 0, 100% 45%, 60% 100%, 0 75%);
  }
  .lid-pattern-edge {
    position: absolute; left: 61px; top: 337px; width: 133px; height: 182px;
    clip-path: polygon(0 0, 100% 0, 100% 45%, 60% 100%, 0 75%);
  }
  .lid-label {
    position: absolute; left: 171px; top: 410px; width: 175px; height: 80px;
    transform: rotate(180deg); transform-origin: 50% 50%;
  }
  .lid-label .band { position: absolute; left: 0; top: 0; width: 175px; height: 41px; }
  .lid-label .wordmark { position: absolute; left: 12px; top: 46px; font-size: 30px; }
  .lid-thumb { position: absolute; left: 363px; top: 432px; width: 28px; height: 28px; border-radius: 50%; background: #c7cdcf; border: 2px solid #e4e8e9; }

  .panel { position: absolute; top: 552px; height: 185px; }
  .panel-main { width: 372px; }
  .panel-side { width: 185px; }

  .wordmark { color: var(--navy); font-weight: 300; letter-spacing: 0.06em; line-height: 1; white-space: nowrap; }
  .panel-main .wordmark { position: absolute; left: 23px; top: 16px; font-size: 32px; }
  .panel-side .wordmark { position: absolute; left: 0; width: 185px; text-align: center; top: 19px; font-size: 23px; }

  .band {
    background: var(--blue); color: #fff; padding: 6px 0 0 23px;
    border-radius: 0 0 8px 0; box-shadow: 5px 4px 0 var(--shade);
  }
  .panel-main .band { position: absolute; left: 0; top: 51px; width: 183px; height: 41px; }
  .panel-side .band { position: absolute; left: 26px; top: 45px; width: 133px; height: 31px; padding: 4px 0 0 10px; }
  .band-title { font-weight: 700; font-size: 10px; line-height: 12px; letter-spacing: 0.05em; }
  .band-sub { font-weight: 400; font-size: 6px; letter-spacing: 0.04em; margin-top: 1px; }
  .panel-side .band-title { font-size: 7.5px; line-height: 9px; }
  .panel-side .band-sub { font-size: 4.6px; }

  .features { position: absolute; left: 23px; top: 102px; list-style: none; }
  .features li {
    font-family: "Open Sans", sans-serif; font-style: italic; font-weight: 600;
    font-size: 5.4px; line-height: 9px; color: var(--blue-text); display: flex; align-items: center; gap: 5px;
  }
  .features svg { width: 7px; height: 6px; }
  .features path { fill: none; stroke: var(--tick); stroke-width: 1.6; }

  .non-medical {
    position: absolute; left: 23px; top: 168px;
    font-family: "Roboto Condensed", sans-serif; font-weight: 700; font-size: 7.5px; color: var(--blue-text);
  }

  .side-pattern {
    position: absolute; left: 239px; top: 0; width: 133px; height: 185px;
    background: linear-gradient(165deg, var(--pattern-light) 0%, #1f6aa8 40%, var(--pattern-dark) 100%);
  }
  .count-badge {
    position: absolute; left: 83px; top: 11px; width: 35px; height: 35px; border-radius: 50%;
    background: var(--navy); border: 2px solid #fff; box-shadow: 0 0 0 1px var(--navy);
    color: #fff; text-align: center; font-family: "Roboto Condensed", sans-serif; font-weight: 700; line-height: 1;
    padding-top: 5px;
  }
  .count-badge .num { font-size: 14px; display: block; }
  .count-badge .unit { font-size: 8px; display: block; }
  .maker { position: absolute; left: 0; width: 133px; top: 160px; text-align: center; color: #fff; }
  .maker-name { font-size: 7px; letter-spacing: 0.03em; font-weight: 400; }
  .maker-place { font-size: 2.6px; letter-spacing: 0.5em; margin-top: 1px; }

  .batch-info { position: absolute; left: 0; width: 185px; top: 86px; text-align: center; font-family: "Roboto", sans-serif; font-size: 9px; line-height: 13px; color: #111; }
  .batch-box { position: absolute; left: 27px; top: 87px; width: 131px; height: 57px; border: 1px solid #555; border-radius: 4px; }
  .maker-dark { position: absolute; left: 0; width: 185px; top: 155px; text-align: center; color: var(--navy); }
  .maker-dark .maker-name { color: var(--blue); }

  .brand-wordmark { position: absolute; left: 0; width: 1200px; top: 1058px; text-align: center; font-size: 78px; }
</style>
</head>
<body>
<div class="canvas">

  <div class="lid-pattern" role="img" aria-label="Faceted blue triangle pattern fading out across the lid corner"></div>

  <svg class="dieline" viewBox="0 0 1200 1200" aria-hidden="true">
    <!-- glue flap -->
    <path d="M60.6,552 L23,554 V732 L60.6,737.5"/>
    <!-- body panels -->
    <rect x="60.6" y="552" width="1113.4" height="185.5"/>
    <path d="M432.5,552 V737.5 M617.5,552 V737.5 M988.75,552 V737.5"/>
    <!-- lid and tuck -->
    <path d="M60.6,552 V347 H432.5 V552"/>
    <path d="M63,347 V325 Q63,306 82,306 H411 Q430,306 430,325 V347"/>
    <path d="M207,344 v4 M285,344 v4"/>
    <!-- top dust flaps -->
    <path d="M432.5,552 L434,512 H604 L617.5,552"/>
    <path d="M759,552 L766,528 Q768,521 775,521 H830 Q838,521 839,528 L846,552"/>
    <path d="M988.75,552 L1002,512 H1172 L1174,552"/>
    <!-- bottom flaps -->
    <path d="M60.6,737.5 L154,839 V866 Q154,879 167,879 H326 Q339,879 339,866 V839 L432.5,737.5"/>
    <path d="M432.5,737.5 V879 H511 Q525,879 525,866 V839 L617.5,737.5"/>
    <path d="M618.5,737.5 V879 H695 Q709,879 709,866 V839 H897 V866 Q897,879 911,879 H986 V737.5"/>
    <path d="M988.75,737.5 L1082,839 V866 Q1082,879 1095,879 H1174 V737.5"/>
    <!-- tear-off opening -->
    <path class="perforation" d="M105,389 H352 Q362,389 362,399 V425 Q397,425 397,446 Q397,466 362,466 V493 Q362,503 352,503 H105 Q95,503 95,493 V399 Q95,389 105,389 Z"/>
  </svg>

  <div class="lid-thumb"></div>
  <div class="lid-label">
    <div class="band">
      <div class="band-title">DISPOSABLE PROTECTIVE<br>FACE MASKS</div>
      <div class="band-sub">3 PLY FACE MASKS WITH EAR LOOP</div>
    </div>
    <div class="wordmark">KELVANO</div>
  </div>

  <!-- front panel -->
  <section class="panel panel-main" style="left:60.6px">
    <div class="wordmark">KELVANO</div>
    <div class="band">
      <div class="band-title">DISPOSABLE PROTECTIVE<br>FACE MASKS</div>
      <div class="band-sub">3 PLY FACE MASKS WITH EAR LOOP</div>
    </div>
    <ul class="features">
      <li><svg viewBox="0 0 7 6"><path d="M0.5,3 L2.7,5 L6.5,0.8"/></svg>Dual Charge Electrostatic fibres for extra filtration</li>
      <li><svg viewBox="0 0 7 6"><path d="M0.5,3 L2.7,5 L6.5,0.8"/></svg>Improved Nose Bridge Strips for better protection</li>
      <li><svg viewBox="0 0 7 6"><path d="M0.5,3 L2.7,5 L6.5,0.8"/></svg>Tri-layer barrier with 3 x 25 g/m2 material</li>
      <li><svg viewBox="0 0 7 6"><path d="M0.5,3 L2.7,5 L6.5,0.8"/></svg>In-house production of filter material for Quality Consistency</li>
    </ul>
    <div class="non-medical">FOR NON- MEDICAL USE</div>
    <div class="side-pattern" role="img" aria-label="Faceted dark blue triangle pattern">
      <div class="count-badge"><span class="num">50</span><span class="unit">pcs</span></div>
      <div class="maker"><div class="maker-name">NORVALE TRADING FZC</div><div class="maker-place">UNITED ARAB EMIRATES</div></div>
    </div>
  </section>

  <!-- batch side panel -->
  <section class="panel panel-side" style="left:432.5px">
    <div class="wordmark">KELVANO</div>
    <div class="band">
      <div class="band-title">DISPOSABLE PROTECTIVE<br>FACE MASKS</div>
      <div class="band-sub">3 PLY FACE MASKS WITH EAR LOOP</div>
    </div>
    <div class="batch-info">LOT # 00000<br>Mfg Date: 000000<br>Exp Date: 000000</div>
  </section>

  <!-- back panel -->
  <section class="panel panel-main" style="left:617.5px">
    <div class="wordmark">KELVANO</div>
    <div class="band">
      <div class="band-title">DISPOSABLE PROTECTIVE<br>FACE MASKS</div>
      <div class="band-sub">3 PLY FACE MASKS WITH EAR LOOP</div>
    </div>
    <ul class="features">
      <li><svg viewBox="0 0 7 6"><path d="M0.5,3 L2.7,5 L6.5,0.8"/></svg>Dual Charge Electrostatic fibres for extra filtration</li>
      <li><svg viewBox="0 0 7 6"><path d="M0.5,3 L2.7,5 L6.5,0.8"/></svg>Improved Nose Bridge Strips for better protection</li>
      <li><svg viewBox="0 0 7 6"><path d="M0.5,3 L2.7,5 L6.5,0.8"/></svg>Tri-layer barrier with 3 x 25 g/m2 material</li>
      <li><svg viewBox="0 0 7 6"><path d="M0.5,3 L2.7,5 L6.5,0.8"/></svg>In-house production of filter material for Quality Consistency</li>
    </ul>
    <div class="non-medical">FOR NON- MEDICAL USE</div>
    <div class="side-pattern" role="img" aria-label="Faceted dark blue triangle pattern">
      <div class="count-badge"><span class="num">50</span><span class="unit">pcs</span></div>
      <div class="maker"><div class="maker-name">NORVALE TRADING FZC</div><div class="maker-place">UNITED ARAB EMIRATES</div></div>
    </div>
  </section>

  <!-- print box side panel -->
  <section class="panel panel-side" style="left:988.75px">
    <div class="wordmark">KELVANO</div>
    <div class="band">
      <div class="band-title">DISPOSABLE PROTECTIVE<br>FACE MASKS</div>
      <div class="band-sub">3 PLY FACE MASKS WITH EAR LOOP</div>
    </div>
    <div class="batch-box"></div>
    <div class="maker-dark"><div class="maker-name">NORVALE TRADING FZC</div><div class="maker-place">UNITED ARAB EMIRATES</div></div>
  </section>

  <div class="wordmark brand-wordmark">KELVANO</div>
</div>
</body>
</html>
```